harvest Ahead Book Cover Design for real estate investment book

I am looking for a Book Cover design for my new book. I would like designs for a hardcover, softcover and Lumora book.

The book deals with real estate and mortgage investments. Looking for a clean, bright simple design. Want to cover to be White with big RED letters. See "Leading from Wonder" book for an example ... see attached.

Target Market(s)

Affluent people with money looking for investment solutions.

Industry/Entity Type

Financial Service

Font styles to use
Serif

Requirements
Must have
• Bright clean design that will be appealing to affluent people.
• Title: harvest AHEAD
• Subtitle: The quiet path to thriving through property holdings
• subsubtitle: Secrets Your Fund Manager Keeps Quiet About...
• Author: Ned Garroway
• My Picture on the inside cover or on the back cover
• Book Description, Author description
Nice to have
• Focus on the Front cover look and feel first. Then we can look at the inside flaps and back cover. I will need to send you text. This is for the full cover. Front. Back. Spine. Inside flaps fro hardcover.

```html
<!DOCTYPE html>
<html lang="en">
<head>
<meta charset="utf-8">
<title>harvest AHEAD — Ned Garroway</title>
<link rel="stylesheet" href="https://fonts.googleapis.com/css2?family=Alfa+Slab+One&family=Cinzel:wght@400&family=Sorts+Mill+Goudy&display=swap">
<style>
  :root {
    --paper: #ffffff;
    --ink: #111111;
    --red-bright: #f0150f;
    --red-mid: #d0140e;
    --red-deep: #9a0e0a;
    --red-gradient: linear-gradient(135deg, var(--red-deep) 0%, var(--red-mid) 40%, var(--red-bright) 60%, var(--red-deep) 100%);
  }
  html, body {
    margin: 0;
    padding: 0;
    overflow: hidden;
    background: var(--paper);
  }
  .cover {
    position: relative;
    width: 800px;
    height: 1200px;
    background: var(--paper);
    overflow: hidden;
  }
  .tagline {
    position: absolute;
    left: 276px;
    top: 40px;
    margin: 0;
    font-family: "Sorts Mill Goudy", "Goudy Old Style", serif;
    font-size: 29px;
    line-height: 34px;
    color: var(--ink);
  }
  .title-word {
    font-family: "Alfa Slab One", "Rockwell", serif;
    font-weight: 400;
    margin: 0;
    position: absolute;
    display: flex;
    flex-direction: column;
    align-items: center;
  }
  .title-letter {
    display: block;
    background: var(--red-gradient);
    -webkit-background-clip: text;
    background-clip: text;
    color: transparent;
  }
  .title-word--vertical {
    left: 130px;
    width: 160px;
    top: 22px;
  }
  .title-word--vertical .title-letter {
    font-size: 168px;
    line-height: 140px;
    height: 140px;
  }
  .title-word--stacked {
    left: 330px;
    width: 300px;
    top: 138px;
  }
  .title-word--stacked .title-letter {
    font-size: 158px;
    line-height: 132px;
    height: 132px;
  }
  .subtitle-disc {
    width: 246px;
    height: 246px;
    margin: 2px 0;
    border-radius: 50%;
    background: radial-gradient(circle at 45% 80%, var(--red-bright) 0%, var(--red-mid) 45%, var(--red-deep) 100%);
    display: flex;
    align-items: center;
    justify-content: center;
    text-align: center;
  }
  .subtitle {
    margin: 0;
    padding: 0 22px;
    font-family: "Sorts Mill Goudy", "Goudy Old Style", serif;
    font-size: 27px;
    line-height: 32px;
    color: var(--paper);
  }
  .author {
    position: absolute;
    left: 0;
    right: 0;
    top: 1070px;
    margin: 0;
    text-align: center;
    font-family: "Cinzel", "Trajan Pro", serif;
    font-weight: 400;
    font-size: 68px;
    letter-spacing: 2px;
    color: var(--ink);
  }
</style>
</head>
<body>
  <main class="cover">
    <p class="tagline">Secrets Your Fund Manager<br>Keeps Quiet About...</p>

    <h1 class="title" aria-label="harvest AHEAD">
      <span class="title-word title-word--vertical" aria-hidden="true">
        <span class="title-letter">h</span>
        <span class="title-letter">a</span>
        <span class="title-letter">r</span>
        <span class="title-letter">v</span>
        <span class="title-letter">e</span>
        <span class="title-letter">s</span>
        <span class="title-letter">t</span>
      </span>
      <span class="title-word title-word--stacked" aria-hidden="true">
        <span class="title-letter">A</span>
        <span class="title-letter">H</span>
        <span class="subtitle-disc"></span>
        <span class="title-letter">E</span>
        <span class="title-letter">A</span>
        <span class="title-letter">D</span>
      </span>
    </h1>

    <div class="title-word title-word--stacked" style="pointer-events:none;">
      <span style="height:264px;display:block;"></span>
      <div class="subtitle-disc" style="background:transparent;">
        <p class="subtitle">The quiet path to thriving through property holdings</p>
      </div>
    </div>

    <p class="author">Ned Garroway</p>
  </main>
</body>
</html>
```